Business card for partnership

Plumbing and hvac company needing a minimal business card. We already have a logo i would like the front of the card just the logo and the back have all info.

Target Market(s)

Commercial facilities

Industry/Entity Type

Plumbing hvac

Contact Information for Business Card

We would like it double sided. Logo big and bold on the front and out info on the back. Our info on back would be name and position phone, email, and location

```html
<!DOCTYPE html>
<html lang="en">
<head>
<meta charset="UTF-8">
<title>Kestrel Mechanical – Business Card</title>
<link href="https://fonts.googleapis.com/css2?family=Montserrat:wght@400;500;700&display=swap" rel="stylesheet">
<style>
  :root {
    --backdrop: #3a3a3a;
    --card-dark: #2e2e2f;
    --card-light: #ffffff;
    --ink-dark: #2b2b2c;
    --ink-light: #ffffff;
    --accent: #ee7a2e;
    --accent-deep: #e0622a;
    --muted: #d9d9d9;
  }
  * { box-sizing: border-box; margin: 0; padding: 0; }
  html, body {
    width: 1200px; height: 1200px; overflow: hidden;
    background: var(--backdrop);
    font-family: "Montserrat", Arial, sans-serif;
  }
  .canvas {
    width: 1200px; height: 1200px;
    display: flex; flex-direction: column; align-items: center; justify-content: center;
    gap: 60px;
  }
  .card {
    width: 840px; height: 480px;
    border-radius: 28px; overflow: hidden;
    box-shadow: 0 18px 40px rgba(0,0,0,0.35);
    position: relative;
  }

  /* Information side */
  .card--info { background: var(--card-dark); display: flex; flex-direction: column; }
  .info-top {
    background: var(--card-light);
    height: 262px;
    display: flex; align-items: center; justify-content: center;
  }
  .accent-rule {
    height: 8px;
    background: linear-gradient(90deg, var(--accent-deep), var(--accent) 60%, #f4a04a);
  }
  .info-bottom {
    flex: 1;
    display: flex; align-items: center; justify-content: space-between;
    padding: 0 60px 0 54px;
  }
  .person {
    border-left: 6px solid var(--accent);
    padding-left: 18px;
  }
  .person-name {
    color: var(--accent);
    font-weight: 500; font-size: 44px; letter-spacing: 1px; line-height: 1;
  }
  .person-role {
    color: var(--ink-light);
    font-weight: 400; font-size: 20px; letter-spacing: 1px; margin-top: 8px;
  }
  .contact-list { list-style: none; display: flex; flex-direction: column; gap: 12px; }
  .contact-item {
    display: flex; align-items: center; gap: 12px;
    color: var(--ink-light); font-size: 21px; font-weight: 400;
  }
  .contact-icon { width: 24px; height: 24px; flex: none; }

  /* Brand lockup */
  .brand { display: flex; align-items: center; gap: 18px; }
  .brand-mark { width: 46px; height: 46px; background: var(--accent); flex: none; }
  .brand-name {
    font-weight: 700; font-size: 50px; letter-spacing: 3px; text-transform: uppercase;
    line-height: 1;
  }
  .card--info .brand-name { color: var(--ink-dark); }

  /* Logo side */
  .card--logo {
    background: var(--card-dark);
    display: flex; align-items: center; justify-content: center;
  }
  .card--logo .brand-mark { width: 66px; height: 66px; }
  .card--logo .brand-name { color: var(--ink-light); font-size: 64px; }
</style>
</head>
<body>
<main class="canvas">

  <section class="card card--info" aria-label="Card back with contact details">
    <div class="info-top">
      <div class="brand">
        <span class="brand-mark" aria-hidden="true"></span>
        <span class="brand-name">Kestrel Mechanical</span>
      </div>
    </div>
    <div class="accent-rule"></div>
    <div class="info-bottom">
      <div class="person">
        <p class="person-name">JOHN DOE</p>
        <p class="person-role">POSITION</p>
      </div>
      <ul class="contact-list">
        <li class="contact-item">
          <svg class="contact-icon" viewBox="0 0 24 24" aria-hidden="true">
            <path fill="#ee7a2e" d="M6.6 10.8a15.1 15.1 0 0 0 6.6 6.6l2.2-2.2a1 1 0 0 1 1-.25 11.4 11.4 0 0 0 3.6.57 1 1 0 0 1 1 1V20a1 1 0 0 1-1 1A17 17 0 0 1 3 4a1 1 0 0 1 1-1h3.5a1 1 0 0 1 1 1c0 1.25.2 2.45.57 3.57a1 1 0 0 1-.25 1z"/>
          </svg>
          (000) 000 0000
        </li>
        <li class="contact-item">
          <svg class="contact-icon" viewBox="0 0 24 24" aria-hidden="true">
            <rect x="2" y="5" width="20" height="14" rx="1" fill="#ee7a2e"/>
            <path d="M2.5 5.5 12 13l9.5-7.5" fill="none" stroke="#2e2e2f" stroke-width="1.6"/>
          </svg>
          email@youremail.com
        </li>
        <li class="contact-item">
          <svg class="contact-icon" viewBox="0 0 24 24" aria-hidden="true">
            <g fill="none" stroke="#ee7a2e" stroke-width="1.8">
              <circle cx="12" cy="12" r="9.5"/>
              <ellipse cx="12" cy="12" rx="4.2" ry="9.5"/>
              <path d="M2.5 12h19M4 7h16M4 17h16"/>
            </g>
          </svg>
          www.yourwebsite.com
        </li>
      </ul>
    </div>
  </section>

  <section class="card card--logo" aria-label="Card front with company name">
    <div class="brand">
      <span class="brand-mark" aria-hidden="true"></span>
      <span class="brand-name">Kestrel Mechanical</span>
    </div>
  </section>

</main>
</body>
</html>
```